Pinecrest 71 Studios needs a web design

We need a website design for a California based visual effects (VFX) company to show potential clients and employees who we are and what we do. We are currently focusing on compositing based tasks such as but not limited to multi-pass composites, green screen extraction, rotoscope, paint fixes and retimes. We like imagery that makes people think of 'California' such as the state flag, sunshine and the beach. The website should send a message that although we are a new company, we are not new to the vfx industry. The website needs to be compatible with mobile devices. We also need the ability to edit and modify the site.

Target Market(s)

Studio executive, producers and potential employees.

Industry/Entity Type

Flag

Coding

Coded - Design and coding required

Number of Pages Required

4 page

Font styles to use
Serif
Sans Serif

Requirements
Must have
• Must have space for company and individual biographies. Must have a page for a credits list and show reel. Must also have space for contact info ex. maps, email, social media.

```html
<!DOCTYPE html>
<html lang="en">
<head>
<meta charset="utf-8">
<title>Pinecrest 71 Studios</title>
<link href="https://fonts.googleapis.com/css2?family=Lato:ital,wght@0,400;0,700;0,900;1,700;1,900&display=swap" rel="stylesheet">
<style>
:root{
  --red:#9c1114;
  --red-soft:#f6e3e3;
  --orange:#b35a06;
  --grey:#6b6b6b;
  --ink:#111;
  --white:#fff;
  --line:#d9d9d9;
  --footer:#060606;
}
*{box-sizing:border-box;margin:0;padding:0}
html,body{width:1200px;height:2214px;overflow:hidden}
body{font-family:"Lato",Arial,sans-serif;color:var(--white);background:var(--white);position:relative}

.sidebar{position:absolute;left:0;top:0;width:188px;height:2214px;background:var(--white);border-right:1px solid var(--line)}
.brand{height:188px;display:flex;align-items:center;justify-content:center;gap:8px;border-bottom:1px solid var(--line)}
.brand-dot{width:16px;height:16px;border-radius:50%;background:var(--red);flex:none}
.brand-name{color:var(--ink);font-weight:900;font-size:17px;line-height:1.15;text-transform:uppercase}
.nav a{display:flex;justify-content:space-between;align-items:center;height:48px;padding:0 12px 0 25px;border-bottom:1px solid var(--line);color:var(--ink);text-decoration:none;font-size:12.5px;font-weight:900;text-transform:uppercase}
.nav a.active{background:var(--red-soft);color:var(--red);border-left:5px solid var(--red);padding-left:20px}
.nav svg{width:16px;height:16px;fill:currentColor}
.social{display:flex;gap:4px;padding:0 0 0 25px;margin-top:37px}
.social span{width:23px;height:23px;border:1.6px solid var(--ink);border-radius:50%}

.main{position:absolute;left:188px;top:0;width:1012px}
.hero{height:469px;background:linear-gradient(180deg,#3b3e42 0%,#6f7376 28%,#8a8c8d 46%,#4a4d50 56%,#2c2f31 75%,#55595c 100%);display:flex;justify-content:center;padding-top:104px}
.hero h1{font-size:33px;font-weight:900;text-align:center;line-height:1.25;width:700px}

.section-title{font-size:19px;font-weight:900;text-transform:uppercase;text-align:center}
.stars{text-align:center;font-size:13px;letter-spacing:2px;line-height:1;margin-top:2px}
.btn{display:inline-block;border:1.5px solid var(--white);border-radius:4px;color:var(--white);font-size:10.5px;font-weight:900;font-style:italic;text-transform:uppercase;text-decoration:none;padding:12px 19px}

.about{height:239px;background:var(--red);text-align:center;padding-top:33px}
.about p{width:890px;margin:16px auto 22px;font-size:13px;line-height:21px}

.what{height:375px;display:flex}
.what-photo{width:506px;background:linear-gradient(135deg,#2b3140 0%,#6c5a4c 40%,#3b4b7a 62%,#1d2026 100%)}
.what-text{flex:1;background:var(--orange);text-align:center;padding:33px 50px 0}
.what-text p{font-size:13px;line-height:21.6px;margin:16px 0 20px}

.featured{height:728px;background:var(--grey);text-align:center;padding-top:52px}
.grid{width:900px;margin:16px auto 23px;display:grid;grid-template-columns:450px 450px;grid-template-rows:253px 253px}
.tile{display:block}
.tile-surf{background:linear-gradient(160deg,#3f8fb6,#86c6d4 50%,#1f6f8f)}
.tile-sweets{background:linear-gradient(135deg,#c3306a,#9ed13a 45%,#41c4d8 70%,#f0b320)}
.tile-couple{background:linear-gradient(120deg,#3a2a22,#9a7a5e 45%,#1c1a1e)}
.tile-project{position:relative;background:linear-gradient(150deg,#4a3b2c,#2d2a24 50%,#5a4d44);display:flex;flex-direction:column;align-items:center;justify-content:center}
.tile-project::before{content:"";position:absolute;inset:0;background:rgba(0,0,0,.35)}
.tile-project *{position:relative}
.tile-project h3{font-size:23px;font-weight:900}
.tile-project em{font-size:13px;font-weight:700;margin-top:4px}
.tile-project svg{width:22px;height:22px;margin-top:18px;fill:none;stroke:var(--white);stroke-width:2}

.contact{height:356px;background:linear-gradient(180deg,#7c8288 0%,#a2a7ab 40%,#7a7468 68%,#9a8e7c 100%);text-align:center;padding-top:34px}
.contact-list{display:flex;justify-content:center;align-items:center;margin-top:15px;font-size:16.5px;font-weight:900;font-style:italic}
.contact-list span{display:flex;align-items:center;gap:4px;padding:0 14px;border-left:1px solid rgba(255,255,255,.7)}
.contact-list span:first-child{border-left:0}
.contact-list svg{width:14px;height:14px;fill:var(--white)}

.footer{height:47px;background:var(--footer);color:#8a8a8a;font-size:11.5px;text-align:center;line-height:47px}
</style>
</head>
<body>

<aside class="sidebar">
  <div class="brand"><span class="brand-dot"></span><span class="brand-name">Pinecrest 71<br>Studios</span></div>
  <nav class="nav">
    <a class="active" href="#">Home<svg viewBox="0 0 16 16"><path d="M8 1 0 8h2v7h4v-4h4v4h4V8h2z"/></svg></a>
    <a href="#">About Us<svg viewBox="0 0 16 16"><circle cx="9" cy="2.5" r="1.8"/><path d="M7 6h3l-2 8h2l-.5 1H5l2-8H6z"/></svg></a>
    <a href="#">Services<svg viewBox="0 0 16 16"><path d="M7 0h2l.4 2.2 1.6.7 1.9-1.3 1.4 1.4-1.3 1.9.7 1.6L16 7v2l-2.2.4-.7 1.6 1.3 1.9-1.4 1.4-1.9-1.3-1.6.7L9 16H7l-.4-2.2-1.6-.7-1.9 1.3-1.4-1.4 1.3-1.9-.7-1.6L0 9V7l2.2-.4.7-1.6-1.3-1.9 1.4-1.4 1.9 1.3 1.6-.7zM8 5a3 3 0 1 0 0 6 3 3 0 0 0 0-6z"/></svg></a>
    <a href="#">Work<svg viewBox="0 0 16 16"><path d="M8 0l2.4 5.3 5.6.6-4.2 3.8 1.2 5.7L8 12.6 3 15.4l1.2-5.7L0 5.9l5.6-.6z"/></svg></a>
    <a href="#">Contac Us<svg viewBox="0 0 16 16"><path d="M0 3h16v1.5L8 9 0 4.5zM0 6l8 4.5L16 6v7H0z"/></svg></a>
  </nav>
  <div class="social" aria-label="Social links"><span></span><span></span><span></span><span></span></div>
</aside>

<main class="main">
  <section class="hero" role="img" aria-label="Stormy sky over the ocean with waves breaking against a long pier">
    <h1>Lorem ipsum dolor sit amet consectetur adipiscing elit pellentesque turpis vel nun.</h1>
  </section>

  <section class="about">
    <h2 class="section-title">About P71</h2>
    <div class="stars">★★★</div>
    <p>Quisque condimentum turpis id ipsum gravida, quis vehicula eros scelerisque. Phasellus aliquam sapien nisi, eu cursus nisl semper et. Nullam rhoncus urna sed sollicitudin elementum. Praesent dolor tellus, scelerisque vitae volutpat a, commodo eu magna. Pellentesque vulputate ligula non erat mattis, id pretium tortor iaculis. Duis commodo semper fermentum. Curabitur nec tristique arcu, at feugiat turpis duis iaculis ligula nec est.</p>
    <a class="btn" href="#">Learn more &amp; meet the team »</a>
  </section>

  <section class="what">
    <div class="what-photo" role="img" aria-label="Smiling artist in a plaid shirt working at a computer in a studio"></div>
    <div class="what-text">
      <h2 class="section-title">What We Do</h2>
      <div class="stars">★★★</div>
      <p>Donec dignissim congue nisl, eget luctus ligula consectetur sit amet. Mauris ac tristique quam, eu molestie augue. Integer ut orci blandit, sodales nisi vitae, vulputate tellus. Vivamus placerat sem augue, vel laoreet nisi euismod et. Integer sit amet gravida tortor, non viverra erat. Sed consectetur arcu eu dui ultrices rhoncus. Class aptent taciti sociosqu ad litora torquent per conubia nostra, per inceptos himenaeos. Nullam suscipit ultrices quam vel porta. Quisque lorem sapien, lobortis id gravida sed, sodales non felis. Donec varius eros sed metus bibendum.</p>
      <a class="btn" href="#">Learn more »</a>
    </div>
  </section>

  <section class="featured">
    <h2 class="section-title">Featured Work</h2>
    <div class="stars">★★★</div>
    <div class="grid">
      <div class="tile tile-surf" role="img" aria-label="Surfer riding inside a curling blue wave"></div>
      <div class="tile tile-sweets" role="img" aria-label="Colourful frosted cupcakes with sprinkles"></div>
      <div class="tile tile-couple" role="img" aria-label="Fashion couple posing in evening wear"></div>
      <div class="tile tile-project" role="img" aria-label="Skate park with graffiti, shown with project overlay">
        <h3>Project Title Goes Here</h3>
        <em>client: Tidewater</em>
        <svg viewBox="0 0 24 24"><path d="M1 12s4-7 11-7 11 7 11 7-4 7-11 7S1 12 1 12z"/><circle cx="12" cy="12" r="3"/></svg>
      </div>
    </div>
    <a class="btn" href="#">View all our works »</a>
  </section>

  <section class="contact" role="img" aria-label="Beachfront homes lined with palm trees under a grey sky">
    <h2 class="section-title">Contact Us</h2>
    <div class="stars">★★★</div>
    <div class="contact-list">
      <span><svg viewBox="0 0 16 16"><path d="M3 0l3 3-1.5 2.5a10 10 0 0 0 6 6L13 10l3 3-2 3C7 16 0 9 0 2z"/></svg>1.800.555.0171</span>
      <span><svg viewBox="0 0 16 16"><path d="M0 3h16v1.5L8 9 0 4.5zM0 6l8 4.5L16 6v7H0z"/></svg>info@Pinecrest71Studios.com</span>
      <span><svg viewBox="0 0 16 16"><path d="M2 0h8l4 4v12H2zM9 1v4h4z"/></svg>webform</span>
      <span><svg viewBox="0 0 16 16"><path d="M8 0a5.5 5.5 0 0 0-5.5 5.5C2.5 10 8 16 8 16s5.5-6 5.5-10.5A5.5 5.5 0 0 0 8 0zm0 3a2.5 2.5 0 1 1 0 5 2.5 2.5 0 0 1 0-5z"/></svg>location</span>
    </div>
  </section>

  <footer class="footer">©2015 Pinecrest 71 Studios.</footer>
</main>

</body>
</html>
```